Bluestone Nine LLC Flyer Design

Marketing Materials for Real Estate Company. This flyer will be used to promote the company throughout the Commercial Real Estate business in the United States. The team has been together for 15 years. We are the middle guys between the Tenant, Broker, and the Owner. In the case of working with a Franchisor, we will be their Plug and Play leasing arm that will assist their new Franchisee's with their site selection, lease negotiations, design and construction management.

Target Market(s)

Real Estate Owners, Franchisor's, and Brokers

Font styles to use
Serif

Colors

Designer to choose colors to be used in the design.

Requirements
Must have
• The flyer must have......
• 1. The Best Leasing Machine On The Planet
• 2. Over the past 15 years our group has completed 4,492 lease transactions resulting in leasing 17,803,114 square feet in shopping centers across the United States.
• 3. Plug and Play Leasing Specialists. We handle the details between when the broker shows up with the space and the tenant and completing the lease negotiations, legal negotiations and documentation, and construction management to Certificate of Occupancy.
• 4. For Information Call Colette Varga at 555-014-2763 or Wendy Falk at 555-017-8302.
Nice to have
• National Tenants the we have completed transactions with....
• Pellmart, Fresh Basket, Harbor Pams, Vexo, Dunn, QV Rendo, Burrasco, Pattersons, Wrap Shack, Brewhorns, Summit Workout, ShipVo, Tredwell, PKN, Halvorsons, Q&L, Ledger Union Bank, Hen Haus-O, Lotus Kitchen, Furvo, Dex-Mart, Fieldly, and Orbit Theaters

```html
<!DOCTYPE html>
<html lang="en">
<head>
<meta charset="utf-8">
<title>Bluestone Nine LLC Flyer</title>
<link rel="stylesheet" href="https://fonts.googleapis.com/css2?family=Open+Sans:wght@400&family=Tinos&display=swap">
<style>
  :root {
    --page: #ffffff;
    --leaf: #77d07f;
    --leaf-deep: #1f7a2a;
    --logo-green: #8dc63f;
    --ink: #111111;
    --skyline-light: #5fbf63;
    --skyline-dark: #0f5a1a;
  }
  * { margin: 0; padding: 0; box-sizing: border-box; }
  html, body { width: 927px; height: 1200px; overflow: hidden; background: var(--page); }
  .page { position: relative; width: 927px; height: 1200px; background: var(--page); }
  .flyer {
    position: absolute; left: 185.3px; top: 150.2px;
    width: 647px; height: 1000px;
    transform: scale(0.8583); transform-origin: top left;
    overflow: hidden; background: var(--page);
    font-family: "Tinos", "Times New Roman", serif; color: var(--ink);
  }
  .waves { position: absolute; inset: 0; }
  .hero {
    position: absolute; left: 0; top: 0; width: 647px; height: 215px;
    background: linear-gradient(180deg, #6b6a66 0%, #8a7358 28%, #4b4038 60%, #2a2622 100%);
    border-bottom: 2px solid var(--logo-green);
  }
  .brand {
    position: absolute; left: 0; top: 150px;
    font-family: "Open Sans", Arial, sans-serif; font-weight: 400;
    font-size: 34px; color: var(--logo-green); letter-spacing: 1px;
  }
  .tagline {
    position: absolute; left: 0; width: 647px; top: 222px; padding-left: 96px;
    font-family: "Open Sans", Arial, sans-serif; font-size: 21px; letter-spacing: 3.6px;
  }
  .photo-round { position: absolute; border-radius: 50%; }
  .photo-city {
    left: 440px; top: 251px; width: 208px; height: 208px;
    background: linear-gradient(180deg, #8fc3ea 0%, #c9d8d6 30%, #4f8a3c 55%, #c9b89a 80%, #8e8a80 100%);
  }
  .photo-office {
    left: -1px; top: 427px; width: 230px; height: 230px;
    background: linear-gradient(160deg, #d9d7d2 0%, #a07a55 45%, #c8c6c0 70%, #8c6a4a 100%);
  }
  .track-record {
    position: absolute; left: 20px; top: 303px; width: 420px;
    font-size: 20px; line-height: 23px;
  }
  .services { position: absolute; left: 245px; top: 481px; width: 395px; }
  .services h2 { font-weight: 400; font-size: 25px; margin-bottom: 14px; }
  .services p { font-size: 19px; line-height: 18px; }
  .tenants { position: absolute; left: 10px; top: 692px; width: 292px; }
  .tenants h3 { font-weight: 400; font-size: 17px; line-height: 17px; margin-bottom: 20px; }
  .tenants p { font-size: 13.5px; line-height: 18px; }
  .contact {
    position: absolute; left: 312px; top: 700px; width: 335px;
    font-family: "Open Sans", Arial, sans-serif; text-align: center;
  }
  .contact-head { display: flex; align-items: center; justify-content: flex-end; gap: 12px; font-size: 22px; padding-right: 4px; }
  .contact-head svg { width: 32px; height: 40px; }
  .contact-lines { margin-top: 18px; font-size: 21px; line-height: 26px; }
  .skyline {
    position: absolute; left: 0; top: 850px; width: 647px; height: 150px;
    background: linear-gradient(180deg, rgba(119,208,127,0) 0%, var(--skyline-light) 35%, var(--leaf-deep) 80%, var(--skyline-dark) 100%);
  }
</style>
</head>
<body>
<div class="page">
  <div class="flyer">
    <svg class="waves" width="647" height="1000" viewBox="0 0 647 1000">
      <rect x="0" y="240" width="647" height="760" fill="var(--leaf)"/>
      <path d="M0,215 H647 V272 C480,238 300,232 0,246 Z" fill="var(--page)"/>
      <path d="M0,402 C200,392 450,440 647,428 L647,455 C450,472 200,432 0,430 Z" fill="var(--page)"/>
      <path d="M0,650 C200,642 450,640 647,632 V690 C500,660 300,652 0,668 Z" fill="var(--page)"/>
    </svg>

    <header class="hero" role="img" aria-label="Aerial photo of a downtown skyline at sunset">
      <div class="brand">Bluestone Nine LLC</div>
    </header>
    <p class="tagline">The Best Leasing Machine On The Planet</p>

    <p class="track-record">&nbsp;Over the past 15 years our group has completed 4,492 lease transactions resulting in leasing 17,803,114 square feet in shopping centers across the United States.</p>
    <div class="photo-round photo-city" role="img" aria-label="Round photo of a city district with green park and buildings"></div>

    <div class="photo-round photo-office" role="img" aria-label="Round photo of an open office with cubicles from above"></div>
    <section class="services">
      <h2>Plug and Play Leasing Specialists</h2>
      <p>We handle the details between when the broker shows up with the space and the tenant and completing the lease negotiations, legal negotiations and documentation, and construc-tion management to Certificate of Occupancy.</p>
    </section>

    <section class="tenants">
      <h3>National Tenants the we have completed transactions with....</h3>
      <p>Pellmart, Fresh Basket, Harbor Pams, Vexo, Dunn, QV Rendo, Burrasco, Pattersons, Wrap Shack, Brewhorns, Summit Workout, ShipVo, Tredwell, PKN, Halvorsons, Q&amp;L, Ledger Union Bank, Hen Haus-O, Lotus Kitchen, Furvo, Dex-Mart, Fieldly, and Orbit Theaters</p>
    </section>

    <section class="contact">
      <div class="contact-head">
        <svg viewBox="0 0 32 40" aria-hidden="true">
          <path d="M6,2 L13,6 L10,14 C9,17 12,25 16,28 L22,24 L28,31 L24,37 C12,38 2,22 3,8 Z" fill="var(--leaf-deep)"/>
        </svg>
        <span>For Information Call</span>
      </div>
      <div class="contact-lines">
        <div>Colette Varga at 555-014-2763</div>
        <div>or</div>
        <div>Wendy Falk at 555-017-8302</div>
      </div>
    </section>

    <div class="skyline" role="img" aria-label="Green city skyline silhouette along the bottom edge"></div>
  </div>
</div>
</body>
</html>
```